Hydraulics Company Business Card Design

Modern business card design for a hydraulics company.
Our company colours are - black, orange and white.
I would like the following contact details included-
Name
Position
Phone number
Email
Website
Street Address

I have attached our company logo.
I would like the back of the card white.

Thank you.

```html
<!DOCTYPE html>
<html lang="en">
<head>
<meta charset="utf-8">
<title>Tallowood Hydraulics – Business Card</title>
<link href="https://fonts.googleapis.com/css2?family=Open+Sans:wght@400;600;700;800&display=swap" rel="stylesheet">
<style>
  :root {
    --orange: #f39c12;
    --black: #070606;
    --white: #ffffff;
    --rule: #8a8a8a;
    --stage: #e9e7e4;
  }
  * { box-sizing: border-box; margin: 0; padding: 0; }
  html, body {
    width: 1200px; height: 900px; overflow: hidden;
    background: var(--stage);
    font-family: "Open Sans", Arial, sans-serif;
  }
  .sheet {
    width: 1200px; height: 900px;
    display: flex; flex-direction: column; align-items: center; justify-content: center;
    gap: 30px;
  }
  .card {
    width: 700px; height: 400px; position: relative;
    box-shadow: 0 6px 18px rgba(0,0,0,0.18);
  }
  .card--front { background: var(--white); }
  .card--back { background: var(--black); color: var(--white); }

  .brand-name {
    font-weight: 800; color: var(--orange); letter-spacing: 0.2px; white-space: nowrap;
  }
  .card--front .brand-name {
    position: absolute; left: 50%; top: 50%; transform: translate(-50%, -50%);
    font-size: 44px;
  }
  .card--back .brand-name {
    position: absolute; right: 48px; top: 58px; font-size: 30px;
  }

  .divider {
    position: absolute; left: 128px; right: 40px; top: 226px;
    height: 1px; background: var(--rule);
  }
  .holder { position: absolute; left: 52px; top: 186px; }
  .holder__name {
    color: var(--orange); font-weight: 700; font-size: 19px;
    text-transform: uppercase; letter-spacing: 0.3px; line-height: 1.1;
  }
  .holder__role { font-size: 15px; margin-top: 4px; padding-left: 18px; }

  .contacts {
    position: absolute; left: 66px; top: 262px; list-style: none;
    font-size: 14.5px; line-height: 1;
  }
  .contacts li { display: flex; align-items: center; gap: 10px; height: 27px; }
  .contacts svg { width: 17px; height: 17px; flex: none; fill: none; stroke: var(--orange); stroke-width: 2; }
  .contacts .icon-solid { fill: var(--orange); stroke: none; }
</style>
</head>
<body>
<main class="sheet">
  <section class="card card--front" aria-label="Card front">
    <span class="brand-name">Tallowood Hydraulics</span>
  </section>

  <section class="card card--back" aria-label="Card back">
    <span class="brand-name">Tallowood Hydraulics</span>
    <div class="divider"></div>
    <div class="holder">
      <p class="holder__name">Daniel Corrigan</p>
      <p class="holder__role">Owner</p>
    </div>
    <ul class="contacts">
      <li>
        <svg viewBox="0 0 24 24" aria-hidden="true"><path class="icon-solid" d="M6.6 10.8a15 15 0 0 0 6.6 6.6l2.2-2.2c.3-.3.7-.4 1-.2 1.1.4 2.3.6 3.6.6.6 0 1 .4 1 1V20c0 .6-.4 1-1 1A17 17 0 0 1 3 4c0-.6.4-1 1-1h3.5c.6 0 1 .4 1 1 0 1.3.2 2.5.6 3.6.1.3 0 .7-.2 1z"/></svg>
        <span>0240118620</span>
      </li>
      <li>
        <svg viewBox="0 0 24 24" aria-hidden="true"><rect x="3" y="6" width="18" height="12" rx="1"/><path d="M3 6l9 7 9-7M3 18l7-6M21 18l-7-6"/></svg>
        <span>info@tallowoodhydraulics.com.au</span>
      </li>
      <li>
        <svg viewBox="0 0 24 24" aria-hidden="true"><circle cx="12" cy="12" r="9"/><ellipse cx="12" cy="12" rx="4" ry="9"/><path d="M3 12h18M5 7h14M5 17h14"/></svg>
        <span>www.tallowoodhydraulics.com.au</span>
      </li>
      <li>
        <svg viewBox="0 0 24 24" aria-hidden="true"><path class="icon-solid" d="M12 2a7 7 0 0 0-7 7c0 5 7 13 7 13s7-8 7-13a7 7 0 0 0-7-7zm0 9.5A2.5 2.5 0 1 1 12 6.5a2.5 2.5 0 0 1 0 5z"/></svg>
        <span>18 Banksia Rd, Riverton NSW 2750</span>
      </li>
    </ul>
  </section>
</main>
</body>
</html>
```